PREVENTING FALLS IN YOUR HOME / MAKING YOUR HOME SAFER

We sell, and install grab bars for only $99 each in the home. Statistics to present: 2.8 million people are treated in emergency rooms annually for falls. 800,000 are hospitalized because of fall injury. 95% of hip fractures are caused by falling. I would like a 1 page marketing piece containing a cartoon like male slipping backwards holding on to shower curtain which is bending curtain rod that cannot support him. Then as a don't and do,same man wisely entering tub using grab bar. Slipping on stairs, trying to grab onto whatever won't hold him would be another scenario.
Included in piece would be above fall statistics separated into bursts, reminder that grab bars can be installed in any room including the garage and a star burst of Only $99, includes bar and installation and

Target Market(s)

over 50 year old market butpredominantly elderly population

Industry/Entity Type

Home Health Care

Font styles to use
Sans Serif

Colors
ec1f27

Requirements
Must have
• instant recognition that a grab bar can prevent serious falls and hip fracture. The cartoon characterization must make instant understanding without reading text
Nice to have
• large print
• concise message
• not a lot of reading to understand
• cartoons in circle with line through don' t circle Ie. no swimming
Should not have
• small print
• congested page

```html
<!DOCTYPE html>
<html lang="en">
<head>
<meta charset="utf-8">
<title>Avoid accidents! – Grab Bars</title>
<link href="https://fonts.googleapis.com/css2?family=Lilita+One&family=Fira+Sans+Extra+Condensed:wght@700;800&display=swap" rel="stylesheet">
<style>
  :root {
    --red: #cc1f24;
    --red-dark: #8e1216;
    --cream: #f6f3d7;
    --yellow: #fff200;
    --yellow-soft: #fdf5a6;
    --white: #ffffff;
    --ink: #1c1c1c;
    --shadow: #b9b6a4;
  }
  * { margin: 0; padding: 0; box-sizing: border-box; }
  html, body { width: 927px; height: 1200px; overflow: hidden; background: var(--cream); }
  .flyer {
    position: relative; width: 927px; height: 1200px; overflow: hidden;
    background: var(--cream);
    font-family: "Fira Sans Extra Condensed", "Arial Narrow", sans-serif;
    font-weight: 700;
  }
  .headline {
    position: absolute; top: 50px; left: 0; width: 927px; text-align: center;
    font-family: "Lilita One", sans-serif; font-weight: 400;
    font-size: 136px; line-height: 1; letter-spacing: -3px;
    color: var(--red);
    -webkit-text-stroke: 0;
    text-shadow:
      -4px -4px 0 var(--white), 4px -4px 0 var(--white), -4px 4px 0 var(--white), 4px 4px 0 var(--white),
      0 -5px 0 var(--white), 0 5px 0 var(--white), -5px 0 0 var(--white), 5px 0 0 var(--white),
      9px 9px 0 var(--shadow);
  }
  .bottom-band { position: absolute; left: 0; top: 0; }
  .cartoon {
    position: absolute; left: 44px; top: 204px; width: 484px; height: 660px;
    background: linear-gradient(180deg, #f4f4f4 0%, #e2e2e2 60%, #f7f7f7 100%);
    border-radius: 30px 30px 60px 20px;
  }
  .burst { position: absolute; }
  .burst-text { position: absolute; text-align: center; line-height: 1; }
  .stat-fall { left: 490px; top: 268px; }
  .stat-fall .burst-text { left: 0; top: 38px; width: 200px; color: var(--red); }
  .stat-fall .big { font-size: 31px; }
  .stat-fall .small { font-size: 16px; margin: 1px 0 4px; }
  .stat-fall .huge { font-size: 42px; line-height: 0.98; }
  .stat-hip { left: 672px; top: 236px; }
  .stat-hip .burst-text { left: 0; top: 42px; width: 200px; color: var(--white); }
  .stat-hip .pct { font-size: 50px; color: var(--yellow); margin-bottom: 4px; }
  .stat-hip .small { font-size: 22px; line-height: 1.12; }
  .product { position: absolute; left: 624px; top: 454px; }
  .product-label {
    position: absolute; left: 618px; top: 642px; width: 244px; height: 116px;
    background: var(--red); border-radius: 6px;
    color: var(--white); font-size: 43px; text-align: center; padding-top: 57px; line-height: 1;
  }
  .product-note {
    position: absolute; left: 622px; top: 766px; width: 242px; height: 252px;
    background: var(--yellow-soft); border-radius: 6px;
    box-shadow: 6px 6px 0 rgba(0,0,0,0.12);
    color: var(--ink); font-size: 27px; line-height: 33px; text-align: center; padding-top: 26px;
  }
  .offer-lead {
    position: absolute; left: 40px; top: 892px; width: 286px; text-align: right;
    color: var(--white); font-size: 35px; line-height: 34px;
    text-shadow: 3px 3px 0 var(--red-dark);
  }
  .benefits {
    position: absolute; left: 40px; top: 972px; width: 286px;
    color: var(--white); font-size: 21px; line-height: 26px; text-align: right;
    text-shadow: 2px 2px 0 var(--red-dark);
  }
  .benefits svg { width: 20px; height: 16px; vertical-align: -1px; margin-right: 2px; }
  .price {
    position: absolute; left: 340px; top: 872px;
    font-family: "Lilita One", sans-serif; font-weight: 400;
    font-size: 182px; line-height: 1; letter-spacing: -6px;
    color: var(--white); text-shadow: 8px 8px 0 var(--red-dark);
  }
  .price .dollar { font-size: 130px; vertical-align: 34px; letter-spacing: -2px; }
  .call {
    position: absolute; left: 0; top: 1060px; width: 927px; text-align: center;
    color: var(--white); line-height: 1;
  }
  .call-line { font-size: 52px; }
  .call-line svg { width: 40px; height: 40px; vertical-align: -2px; margin: 0 2px 0 6px; }
  .web-line { font-size: 33px; margin-top: 6px; }
</style>
</head>
<body>
<main class="flyer">
  <h1 class="headline">Avoid accidents!</h1>

  <svg class="bottom-band" width="927" height="1200" viewBox="0 0 927 1200" aria-hidden="true">
    <path d="M0 872 C 230 800, 500 770, 700 785 C 800 792, 880 808, 927 830 L927 1200 L0 1200 Z" fill="var(--red)"/>
  </svg>

  <div class="cartoon" role="img" aria-label="Cartoon of a man slipping in the shower, clutching a shower curtain as he falls backwards into the tub"></div>

  <div class="burst stat-fall">
    <svg width="200" height="200" viewBox="0 0 200 200" aria-hidden="true">
      <circle cx="100" cy="100" r="94" fill="var(--yellow)"/>
      <circle cx="100" cy="100" r="97" fill="none" stroke="var(--yellow)" stroke-width="6" stroke-dasharray="4 4"/>
    </svg>
    <div class="burst-text">
      <div class="big">800,000</div>
      <div class="small">hospitalized due to</div>
      <div class="huge">FALL<br>INJURY</div>
    </div>
  </div>

  <div class="burst stat-hip">
    <svg width="200" height="200" viewBox="0 0 200 200" aria-hidden="true">
      <circle cx="100" cy="100" r="94" fill="var(--red)"/>
      <circle cx="100" cy="100" r="97" fill="none" stroke="var(--red)" stroke-width="6" stroke-dasharray="4 4"/>
    </svg>
    <div class="burst-text">
      <div class="pct">95%</div>
      <div class="small">of hip fractures<br>are caused by<br>falling!</div>
    </div>
  </div>

  <svg class="product" width="220" height="220" viewBox="0 0 220 220" role="img" aria-label="Photo of a brushed steel grab bar">
    <defs>
      <radialGradient id="product-bg" cx="50%" cy="45%" r="60%">
        <stop offset="0%" stop-color="#ffffff"/>
        <stop offset="70%" stop-color="#cde9f3"/>
        <stop offset="100%" stop-color="#8fcbe0"/>
      </radialGradient>
    </defs>
    <circle cx="110" cy="110" r="104" fill="url(#product-bg)" stroke="var(--yellow)" stroke-width="5"/>
  </svg>

  <div class="product-label">GRAB BARS</div>

  <div class="product-note">FOR YOUR<br>BATHROOM, BY<br>YOUR STAIRS, OR<br>ANYWHERE IN<br>YOUR HOME WHERE<br>SLIPS CAN HAPPEN!</div>

  <div class="offer-lead">PROFESSIONALLY<br>INSTALLED FROM</div>
  <div class="benefits">
    <svg viewBox="0 0 20 16" aria-hidden="true"><path d="M2 8 L8 14 L18 2" fill="none" stroke="var(--yellow)" stroke-width="4" stroke-linecap="round" stroke-linejoin="round"/></svg>STABILITY
    <svg viewBox="0 0 20 16" aria-hidden="true"><path d="M2 8 L8 14 L18 2" fill="none" stroke="var(--yellow)" stroke-width="4" stroke-linecap="round" stroke-linejoin="round"/></svg>EXTRA SUPPORT<br>
    <svg viewBox="0 0 20 16" aria-hidden="true"><path d="M2 8 L8 14 L18 2" fill="none" stroke="var(--yellow)" stroke-width="4" stroke-linecap="round" stroke-linejoin="round"/></svg>AFFORDABLE PEACE OF MIND
  </div>

  <div class="price"><span class="dollar">$</span>99</div>

  <div class="call">
    <div class="call-line">Order yours!<svg viewBox="0 0 24 24" aria-hidden="true"><path d="M6.6 10.8c1.4 2.8 3.8 5.1 6.6 6.6l2.2-2.2c.3-.3.7-.4 1-.2 1.1.4 2.3.6 3.6.6.6 0 1 .4 1 1V20c0 .6-.4 1-1 1C10.6 21 3 13.4 3 4c0-.6.4-1 1-1h3.5c.6 0 1 .4 1 1 0 1.3.2 2.5.6 3.6.1.3 0 .7-.2 1L6.6 10.8z" fill="var(--yellow)"/></svg>800-555-0147</div>
    <div class="web-line">or visit www.safestepathome.com</div>
  </div>
</main>
</body>
</html>
```